Business Card Design for Engineering Firm

Need a business card design for small mechanical and plumbing engineering form based in Utah. Design should be customizable for all employees.

```html
<!DOCTYPE html>
<html lang="en">
<head>
<meta charset="utf-8">
<title>Harlow Engineering – Business Card</title>
<link href="https://fonts.googleapis.com/css2?family=Lato:wght@400;700;900&display=swap" rel="stylesheet">
<style>
  :root {
    --stage: #e6e6e6;
    --card: #ffffff;
    --brand-red: #7d0a0a;
    --graphite: #4a4a4a;
    --ink: #3a3a3a;
    --foil-light: #f4f4f4;
    --foil-mid: #d9d9d9;
    --foil-dark: #c2c2c2;
  }
  * { box-sizing: border-box; margin: 0; padding: 0; }
  html, body {
    width: 1200px; height: 800px; overflow: hidden;
    background: var(--stage);
    font-family: "Lato", Arial, sans-serif;
  }
  .stage {
    width: 1200px; height: 800px;
    display: flex; align-items: center; justify-content: center; gap: 30px;
  }
  .card {
    position: relative;
    width: 560px; height: 320px;
    border-radius: 22px;
    overflow: hidden;
    background: var(--card);
    box-shadow: 0 6px 18px rgba(0,0,0,.18);
  }
  .corner-accent { position: absolute; inset: 0; width: 100%; height: 100%; }

  /* front */
  .brand-block {
    position: absolute; left: 40px; top: 0; width: 250px; height: 100%;
    display: flex; align-items: center; justify-content: center; gap: 10px;
  }
  .brand-square { width: 18px; height: 18px; background: var(--brand-red); flex: none; }
  .brand-name {
    font-weight: 900; color: var(--brand-red);
    font-size: 24px; letter-spacing: .5px; text-transform: uppercase; line-height: 1.1;
  }
  .divider {
    position: absolute; left: 300px; top: 92px; width: 1px; height: 136px;
    background: var(--brand-red);
  }
  .contact-block {
    position: absolute; left: 322px; top: 70px; width: 220px;
    color: var(--ink);
  }
  .person-name {
    font-weight: 900; color: var(--brand-red);
    font-size: 22px; text-transform: uppercase; letter-spacing: .3px;
  }
  .person-title { font-size: 14px; margin-top: 2px; }
  .address { font-size: 11.5px; line-height: 1.45; margin-top: 12px; }
  .contact-list { list-style: none; margin-top: 8px; font-size: 11.5px; line-height: 1.65; }
  .contact-list li { display: flex; align-items: center; gap: 7px; }
  .contact-list svg { width: 10px; height: 10px; fill: var(--brand-red); flex: none; }

  /* back */
  .foil-pattern {
    position: absolute; inset: 0;
    background: linear-gradient(135deg, var(--foil-light) 0%, var(--foil-mid) 40%, var(--foil-light) 60%, var(--foil-dark) 100%);
  }
  .back-brand {
    position: absolute; right: 34px; bottom: 70px;
    display: flex; align-items: center; gap: 8px;
    background: rgba(255,255,255,.75); padding: 8px 12px;
  }
  .back-brand .brand-name { font-size: 14px; }
  .back-brand .brand-square { width: 12px; height: 12px; }
</style>
</head>
<body>
<main class="stage">

  <section class="card card-front" aria-label="Business card front">
    <svg class="corner-accent" viewBox="0 0 560 320" aria-hidden="true">
      <polygon points="498,0 560,0 560,118" fill="var(--brand-red)"/>
      <line x1="486" y1="0" x2="560" y2="140" stroke="var(--graphite)" stroke-width="4"/>
      <polygon points="0,202 0,320 62,320" fill="var(--brand-red)"/>
      <line x1="0" y1="180" x2="74" y2="320" stroke="var(--graphite)" stroke-width="4"/>
    </svg>

    <div class="brand-block">
      <span class="brand-square"></span>
      <span class="brand-name">Harlow Engineering</span>
    </div>

    <div class="divider"></div>

    <div class="contact-block">
      <h1 class="person-name">Daniel Reyes</h1>
      <p class="person-title">Founder &amp; CEO</p>
      <p class="address">48 Canyon Ridge Rd.<br>Provo, UT 84601</p>
      <ul class="contact-list">
        <li><svg viewBox="0 0 10 10"><path d="M2 0.5 L3.6 0.5 L4.3 2.8 L3.2 3.7 Q4.2 5.8 6.3 6.8 L7.2 5.7 L9.5 6.4 L9.5 8 Q9.5 9.5 8 9.5 Q0.5 9 0.5 2 Q0.5 0.5 2 0.5Z"/></svg>(555) 210-4431</li>
        <li><svg viewBox="0 0 10 10"><path d="M2.5 0 H7.5 V10 H2.5Z M3.3 1 V8 H6.7 V1Z"/></svg>(555) 210-4432</li>
        <li><svg viewBox="0 0 10 10"><path d="M0 2 H10 V8 H0Z M0.8 2.6 L5 5.6 L9.2 2.6Z" fill-rule="evenodd"/></svg>hello@harloweng.com</li>
        <li><svg viewBox="0 0 10 10"><circle cx="5" cy="5" r="4.5"/><path d="M0.5 5 H9.5 M5 0.5 V9.5" stroke="#fff" stroke-width="0.8"/></svg>harloweng.com</li>
      </ul>
    </div>
  </section>

  <section class="card card-back" aria-label="Business card back">
    <div class="foil-pattern" role="img" aria-label="Silver foil repeating geometric pattern across the whole card"></div>
    <div class="back-brand">
      <span class="brand-square"></span>
      <span class="brand-name">Harlow Engineering</span>
    </div>
  </section>

</main>
</body>
</html>
```